Book Cover "Venice"

Creation of a cover (14 x 20.5 cm + bleed area) for a book:
Image: “BrumeVerte” (Tiff joined)
AUTHOR: Maribel Quonte
TITLE: The murmurs of Oldmere
PUBLISHER: Editions Plavoc (AT THE BOTTOM OF THE COVER)
Updates

Target Market(s)

Readers of romantic novels

Industry/Entity Type

Book

```html
<!DOCTYPE html>
<html lang="fr">
<head>
<meta charset="utf-8">
<title>Les murmures d’Oldmere — Maribel Quonte</title>
<link rel="stylesheet" href="https://fonts.googleapis.com/css2?family=Cinzel:wght@600;700;800&display=swap">
<style>
  :root {
    --page-bg: #ffffff;
    --cover-dark: #4a4846;
    --cover-darker: #3a3836;
    --sky-red: #d2463e;
    --sky-deep: #c23a36;
    --sky-orange: #e8806a;
    --dusk-mauve: #8a4a46;
    --skyline-shadow: #4e4746;
    --title-red: #d5504a;
    --band-light: #dc685c;
    --band-deep: #b93a30;
    --author-ivory: #f4ece6;
    --publisher-ink: #3b2b28;
    --rule-light: #d9d6d2;
  }
  html, body {
    margin: 0;
    padding: 0;
    width: 1078px;
    height: 1200px;
    overflow: hidden;
    background: var(--page-bg);
  }
  .cover {
    position: absolute;
    left: 160px;
    top: 60px;
    width: 757px;
    height: 1080px;
    overflow: hidden;
    background: linear-gradient(90deg, #5a5855 0%, var(--cover-dark) 40%, var(--cover-darker) 100%);
    font-family: "Cinzel", serif;
  }
  .cover-photo {
    position: absolute;
    left: 0;
    top: 0;
    width: 100%;
    height: 640px;
    background:
      radial-gradient(ellipse 38% 30% at 45% 62%, rgba(70,64,63,0.85) 0%, rgba(70,64,63,0) 100%),
      radial-gradient(ellipse 60% 34% at 40% 70%, rgba(78,71,70,0.9) 0%, rgba(78,71,70,0) 100%),
      radial-gradient(ellipse 45% 30% at 18% 8%, rgba(232,128,106,0.9) 0%, rgba(232,128,106,0) 100%),
      radial-gradient(ellipse 40% 25% at 85% 30%, rgba(214,72,62,0.8) 0%, rgba(214,72,62,0) 100%),
      linear-gradient(180deg,
        var(--sky-red) 0%,
        var(--sky-deep) 28%,
        var(--dusk-mauve) 50%,
        var(--skyline-shadow) 66%,
        rgba(74,72,70,0.6) 84%,
        rgba(74,72,70,0) 100%);
  }
  .author {
    position: absolute;
    top: 24px;
    left: 0;
    width: 100%;
    text-align: center;
    color: var(--author-ivory);
    font-weight: 700;
    font-size: 40px;
    letter-spacing: 0.5px;
    margin: 0;
  }
  .title {
    margin: 0;
    color: var(--title-red);
    font-weight: 700;
  }
  .title-line {
    position: absolute;
    left: 0;
    width: 100%;
    text-align: center;
    line-height: 1;
    display: block;
    white-space: nowrap;
  }
  .title-les { top: 538px; font-size: 124px; }
  .title-main { top: 668px; font-size: 108px; letter-spacing: -2px; }
  .title-de { top: 790px; font-size: 54px; }
  .title-place { top: 864px; font-size: 130px; letter-spacing: -4px; }
  .title-rule {
    position: absolute;
    top: 812px;
    left: 20px;
    width: 717px;
    height: 6px;
  }
  .publisher-band {
    position: absolute;
    left: 0;
    bottom: 0;
    width: 100%;
    height: 86px;
    background: linear-gradient(90deg, var(--band-light), var(--band-deep));
    display: flex;
    align-items: center;
    justify-content: center;
  }
  .publisher {
    margin: 0;
    color: var(--publisher-ink);
    font-weight: 700;
    font-size: 30px;
  }
</style>
</head>
<body>
  <main class="cover">
    <div class="cover-photo" role="img" aria-label="Photograph: silhouette of a domed church and lit street lamps against a red sunset sky"></div>
    <p class="author">Maribel Quonte</p>
    <svg class="title-rule" viewBox="0 0 717 6" aria-hidden="true">
      <polygon points="0,3 296,0.5 296,5.5" fill="var(--rule-light)"/>
      <polygon points="717,3 421,0.5 421,5.5" fill="var(--rule-light)"/>
    </svg>
    <h1 class="title">
      <span class="title-line title-les">LES</span>
      <span class="title-line title-main">MURMURES</span>
      <span class="title-line title-de">D’</span>
      <span class="title-line title-place">OLDMERE</span>
    </h1>
    <footer class="publisher-band">
      <p class="publisher">Editions Plavoc</p>
    </footer>
  </main>
</body>
</html>
```